Instructions for nurses on how to give a report on each shift

I have a 2-page reference sheet that needs to be updated to look more aesthetically pleasing.

Target Market(s)

Healthcare, nurses

Industry/Entity Type

Healthcare

Font styles to use
Sans Serif

Requirements
Must have
• Please make sure it is easy to read, the content is well organized and has a flow to it. Please also pick colors that would coordinate with our website www.ovtrime.org (so mainly navy and white or off-white with accent colors.) Please make sure to add accent colors to break up the content. The BORSK name and title at the top should remain on the page but I'm not married to the star or logo style. You can do what you think looks best there. Way at the bottom in fine print, I would like for you to add OVTRIME © 2019 All rights reserved.

```html
<!DOCTYPE html>
<html lang="en">
<head>
<meta charset="utf-8">
<title>BORSK – Shift Report Reference</title>
<link href="https://fonts.googleapis.com/css2?family=Fira+Sans:wght@700&family=Source+Sans+3:ital,wght@0,400;0,700;1,400&display=swap" rel="stylesheet">
<style>
  :root {
    --navy: #163a5c;
    --brand-blue: #1f6fb5;
    --panel-start: #1d4669;
    --panel-end: #6c9fc7;
    --bg-center: #ffffff;
    --bg-edge: #bfe0f3;
    --white: #ffffff;
    --fine-print: #6d7f8c;
  }
  html, body {
    margin: 0;
    padding: 0;
    width: 1200px;
    height: 849px;
    overflow: hidden;
  }
  .sheet {
    position: relative;
    width: 1200px;
    height: 849px;
    background: radial-gradient(ellipse 60% 75% at 28% 55%, var(--bg-center) 0%, #e6f4fb 45%, var(--bg-edge) 100%);
    font-family: "Source Sans 3", Arial, sans-serif;
    overflow: hidden;
  }
  .brand {
    position: absolute;
    left: 449px;
    top: 54px;
  }
  .brand-name {
    display: block;
    margin-left: 40px;
    font-family: "Source Sans 3", Arial, sans-serif;
    font-weight: 400;
    font-size: 40px;
    line-height: 44px;
    letter-spacing: 1px;
    color: var(--brand-blue);
  }
  .brand-tagline {
    margin: 10px 0 0;
    font-family: "Source Sans 3", Arial, sans-serif;
    font-weight: 400;
    font-size: 15px;
    line-height: 18px;
    color: var(--navy);
  }
  .motto {
    position: absolute;
    left: 40px;
    top: 158px;
    width: 420px;
    margin: 0;
    text-align: center;
    font-family: "Fira Sans", Arial, sans-serif;
    font-weight: 700;
    font-size: 50px;
    color: var(--navy);
  }
  .motto span {
    display: block;
    height: 115.5px;
    line-height: 62px;
  }
  .panel {
    position: absolute;
    left: 443px;
    width: 592px;
    box-sizing: border-box;
    padding: 3px 10px 0 9px;
    border-radius: 14px;
    background: linear-gradient(90deg, var(--panel-start) 0%, #2e5b82 40%, var(--panel-end) 100%);
    color: var(--white);
    font-size: 14px;
    line-height: 15.6px;
  }
  .panel h2 {
    margin: 0;
    font-size: 14px;
    font-weight: 700;
    text-decoration: underline;
  }
  .panel ul {
    list-style: none;
    margin: 0;
    padding: 0;
  }
  .panel li::before { content: "•"; }
  .panel--objectives { top: 174px; height: 101px; }
  .panel--outcomes { top: 284px; height: 101px; }
  .panel--who { top: 392px; height: 117px; }
  .panel--when { top: 517px; height: 58px; }
  .panel--where { top: 581px; height: 38px; }
  .panel--tips { top: 627px; height: 165px; }
  .fine-print {
    position: absolute;
    right: 42px;
    top: 813px;
    margin: 0;
    font-style: italic;
    font-size: 11px;
    color: var(--fine-print);
  }
</style>
</head>
<body>
<main class="sheet">
  <header class="brand">
    <span class="brand-name">BORSK</span>
    <p class="brand-tagline">Building Openness, Respect,<br>Safety and Knowledge</p>
  </header>

  <h1 class="motto">
    <span>When “I”</span>
    <span>is replaced by</span>
    <span>“WE”</span>
    <span>Even illness</span>
    <span>becomes</span>
    <span>wellness.</span>
  </h1>

  <section class="panel panel--objectives">
    <h2>OBJECTIVES:</h2>
    <ul>
      <li>Accountability: Declare roles and assignments</li>
      <li>Advocacy: Identify patient needs</li>
      <li>Critical Thinking: Prioritize and recognize obstacles</li>
      <li>Communication: Share important information</li>
      <li>Collaboration: Utilize an interdisciplinary approach</li>
    </ul>
  </section>

  <section class="panel panel--outcomes">
    <h2>OUTCOMES:</h2>
    <ul>
      <li>Share best practices</li>
      <li>Improve communication</li>
      <li>Promote cohesiveness</li>
      <li>Increase staff morale</li>
      <li>Enhance patient and organizational outcomes</li>
    </ul>
  </section>

  <section class="panel panel--who">
    <h2>WHO:</h2>
    <ul>
      <li>All nurses on the unit</li>
      <li>All nursing support staff (CNA/MA/HCT)</li>
      <li>Administrator</li>
      <li>Director of Nursing</li>
      <li>Head of pertinent disciplines (Dietary, Social Work, Physical Therapy, Engineering, Central Supply, etc.)</li>
    </ul>
  </section>

  <section class="panel panel--when">
    <h2>WHEN:</h2>
    <ul>
      <li>Every morning (assign a meeting time for each unit )</li>
      <li>Keep meetings within 15 minutes in length</li>
    </ul>
  </section>

  <section class="panel panel--where">
    <h2>WHERE:</h2>
    <ul>
      <li>Nursing station on each unit</li>
    </ul>
  </section>

  <section class="panel panel--tips">
    <h2>HELPFUL TIPS:</h2>
    <ul>
      <li>Assign a meeting facilitator (usually the administrator of the facility)</li>
      <li>Standing during meetings keeps the meetings short and to the point</li>
      <li>Keeping meetings within 15 minutes emphasizes being prepared and direct</li>
      <li>Keep meeting times consistent (morning is best)</li>
      <li>Do not begin until everyone is present (minimizes stragglers)</li>
      <li>Avoid discussing personal concerns</li>
      <li>Include reminders for in-services, meetings, etc. and updates towards the end of the meeting</li>
      <li>Always conclude with achievements, milestones, praise, words of encouragement, motivational quote, etc.</li>
    </ul>
  </section>

  <p class="fine-print">OVTRIME © 2019 All rights reserved.</p>
</main>
</body>
</html>
```